Marisol Dune - Australia's Sexiest Lingerie

Dear designer!
Myself and my business partner Mari Holloway (google her or checkout her insta account @mariholloway) are launching a new lingerie company called Marisol Dune in 4 months and are in dire need of quality graphic design. If we like your designs we'd love to grow our brand with you and hopefully you'd be proud to have us in your portfolio. We're expecting big things very soon!
We like the idea of cursive writing (script fonts). Something very elegant to match an elegant name - Marisol Dune.
https://larkspurintimates.example and http://hollowtideunderwear.example are two designs that appeal to us.
Our slogan is "Australia's Sexiest Lingerie" and our 2 logo's are the initials "MD" and what they stand for "Marisol Dune". The "MD" will eventually be used on all the products as a jewellery charm. Please incorporate these into the web design somehow.
The final design should be simple and beautiful.
Thanks very much designer, we look forward to seeing your work!
Updates
We have some fantastic results so far, thank you for the submissions. For those yet to submit, please know that the best design will receive our ongoing business directly. Still 2 weeks to pick the best. We look forward to seeing your piece of art. Added Sunday, June 7, 2015
Target Market(s)
Women 18 - 35
Industry/Entity Type
Retail
Contact Information for Business Card
CARD 1:
Marisol Dune Pty Ltd
(Logo)
Colin Brevik
Co-founder and Director
0431 857 204
colin@marisol-dune.example
CARD 2:
Marisol Dune Pty Ltd
(Logo)
Marisol Dune Holloway
Co-founder and Director
0417 263 590
mari@marisol-dune.example
Logo Text
Australia's Sexiest Lingerie
Coding
Coded - Design and coding required
Number of Pages Required
1 page
Requirements
Must have
- 1 x 'MD" Logo
- 1 x 'Marisol Dune' Logo
- 1 x 'Australia's Sexiest Lingerie' Slogan

```html
<!DOCTYPE html>
<html lang="en">
<head>
<meta charset="utf-8">
<title>Marisol Dune – Australia's Sexiest Lingerie</title>
<link rel="stylesheet" href="https://fonts.googleapis.com/css2?family=Josefin+Sans:wght@300;400;600&family=PT+Sans+Narrow:wght@400&family=Open+Sans:wght@400;600&display=swap">
<style>
  :root {
    --navy: #2b2660;
    --ink: #333333;
    --muted: #777777;
    --soft: #9a9a9a;
    --rule: #e2e2e2;
    --band: #ececec;
    --footer: #f8f8f8;
    --dark-btn: #3a3a3a;
    --sale-red: #f20d0d;
    --sky-top: #1d7fd6;
    --sky-mid: #5db3ee;
    --sea: #0e63b0;
    --white: #ffffff;
    --social-1: #8a6a55;
    --social-2: #2aa3e0;
    --social-3: #c8232c;
    --social-4: #3b5998;
  }
  * { box-sizing: border-box; margin: 0; padding: 0; }
  html, body { width: 988px; height: 1200px; overflow: hidden; background: var(--white); }
  body { position: relative; font-family: "Open Sans", Arial, sans-serif; color: var(--ink); }
  .abs { position: absolute; }

  /* top utility bar */
  .utility { top: 14px; font-size: 8px; color: var(--muted); white-space: nowrap; }
  .utility b { color: var(--ink); font-weight: 600; }
  .utility-links { top: 15px; left: 517px; display: flex; gap: 15px; font-size: 7.5px; letter-spacing: .4px; color: var(--muted); }
  .utility-divider { top: 11px; left: 502px; width: 1px; height: 16px; background: #999; }
  .social { display: flex; gap: 3px; }
  .social span { width: 14px; height: 14px; display: block; }
  .social span:nth-child(1) { background: var(--social-1); }
  .social span:nth-child(2) { background: var(--social-2); }
  .social span:nth-child(3) { background: var(--social-3); }
  .social span:nth-child(4) { background: var(--social-4); }

  /* brand */
  .brand-mark { left: 184px; top: 38px; width: 52px; height: 52px; border: 5px solid var(--navy); border-radius: 50%; }
  .brand-name { left: 108px; top: 104px; width: 208px; text-align: center; font-family: "Josefin Sans", sans-serif; font-weight: 400; font-size: 22px; letter-spacing: 2.2px; color: var(--navy); }
  .brand-slogan { left: 108px; top: 131px; width: 208px; text-align: center; font-family: "Open Sans", sans-serif; font-weight: 600; font-size: 10.5px; color: var(--navy); letter-spacing: .3px; }

  .shipping { left: 582px; top: 62px; font-family: "Josefin Sans", sans-serif; color: #444; }
  .shipping strong { display: block; font-weight: 400; font-size: 16px; letter-spacing: 1px; }
  .shipping small { display: block; font-size: 9px; margin-top: -1px; }
  .cart-icon { left: 744px; top: 53px; }
  .cart { left: 786px; top: 58px; font-family: "Josefin Sans", sans-serif; color: #555; font-size: 12px; line-height: 15px; }
  .cart small { display: block; font-size: 9.5px; color: var(--muted); }

  /* nav */
  .nav { left: 418px; top: 116px; width: 460px; height: 23px; background: #f3f3f3; display: flex; align-items: center; font-family: "Josefin Sans", sans-serif; font-size: 9.5px; letter-spacing: 1px; color: #555; }
  .nav a { color: inherit; text-decoration: none; }
  .nav .current { background: var(--navy); color: var(--white); width: 56px; height: 23px; display: flex; align-items: center; justify-content: center; }
  .nav ul { list-style: none; display: flex; }
  .nav li { padding: 0 10px; border-left: 1px solid #999; line-height: 9px; }
  .nav li:first-child { border-left: 0; padding-left: 13px; }

  /* hero */
  .hero { left: 0; top: 151px; width: 988px; height: 468px; overflow: hidden;
    background: linear-gradient(180deg, var(--sky-top) 0%, var(--sky-mid) 45%, #a9d6f5 62%, var(--sea) 68%, #1a7cc6 82%, #3f9ad6 100%); }
  .hero-figure { left: 150px; top: 0; width: 360px; height: 468px;
    background: radial-gradient(ellipse at 50% 50%, rgba(224,170,130,.55) 0%, rgba(224,170,130,.25) 45%, rgba(224,170,130,0) 70%); }
  .sale-flag { right: 99px; top: 91px; }
  .sale-flag span { position: absolute; right: 20px; top: 30px; font-family: "PT Sans Narrow", sans-serif; font-size: 36px; color: var(--white); }
  .hero-title { right: 99px; top: 190px; text-align: right; font-family: "PT Sans Narrow", sans-serif; color: var(--white); text-shadow: 0 1px 2px rgba(0,0,0,.25); }
  .hero-title h1 { font-weight: 400; font-size: 55px; letter-spacing: 2px; line-height: 58px; }
  .hero-title p { font-size: 33px; letter-spacing: 1.5px; line-height: 40px; margin-top: 6px; }
  .btn-dark { background: var(--dark-btn); color: var(--white); font-family: "PT Sans Narrow", sans-serif; display: flex; align-items: center; justify-content: center; }
  .hero-btn { left: 776px; top: 318px; width: 112px; height: 34px; font-size: 17px; }

  /* promo band */
  .promo { left: 0; top: 619px; width: 988px; height: 113px; background: linear-gradient(180deg, #ffffff 0%, #f6f6f6 50%, var(--band) 50%, var(--band) 100%); font-family: "Josefin Sans", sans-serif; color: #333; }
  .promo-divider { left: 364px; top: 0; width: 1px; height: 113px; background: #d4d4d4; }
  .promo-collections { left: 128px; top: 30px; font-size: 16px; font-weight: 400; letter-spacing: 1.2px; line-height: 30px; white-space: nowrap; }
  .promo-collections .year { font-size: 24px; font-weight: 300; letter-spacing: 1px; margin-right: 4px; }
  .promo-group { top: 28px; display: flex; align-items: center; gap: 12px; white-space: nowrap; }
  .promo-sale { left: 402px; }
  .promo-hot { left: 664px; }
  .promo-big { font-size: 44px; font-weight: 300; letter-spacing: 1px; line-height: 50px; }
  .promo-sub { font-size: 18px; line-height: 20px; letter-spacing: 1px; font-weight: 300; }
  .promo-btn { width: 88px; height: 20px; margin-top: 2px; font-family: "Josefin Sans", sans-serif; font-size: 11px; letter-spacing: 1px; }

  /* products */
  .product { top: 751px; width: 143px; text-align: center; }
  .product-photo { width: 143px; height: 216px; }
  .product-name { margin-top: 25px; font-family: Arial, sans-serif; font-size: 9.5px; color: #444; }
  .product-price { margin-top: 5px; font-family: "Times New Roman", serif; font-weight: 700; font-size: 10.5px; color: #222; }
  .product-rule { top: 751px; width: 1px; height: 269px; background: var(--rule); }

  /* footer */
  .footer { left: 0; top: 1044px; width: 988px; height: 118px; background: var(--footer); border-top: 1px solid var(--rule); border-bottom: 1px solid var(--rule); }
  .footer-col { top: 1058px; font-family: "Josefin Sans", sans-serif; }
  .footer-col h3 { font-weight: 400; font-size: 11px; letter-spacing: 1px; color: #555; margin-bottom: 9px; }
  .footer-col li { list-style: none; font-size: 8.5px; color: var(--soft); line-height: 16px; }
  .copyright { left: 115px; top: 1171px; font-family: "Josefin Sans", sans-serif; font-size: 9.5px; color: #444; letter-spacing: .5px; }
</style>
</head>
<body>

<header>
  <div class="abs utility" style="left:305px">Welcome You can <b>Login</b> or <b>Create an account</b></div>
  <div class="abs utility-divider"></div>
  <nav class="abs utility-links">
    <span>WISHLIST (0)</span><span>MY ACCOUNT</span><span>SHOPPING CART</span><span>LOGOUT</span>
  </nav>
  <div class="abs social" style="left:799px; top:10px"><span></span><span></span><span></span><span></span></div>

  <div class="abs brand-mark"></div>
  <div class="abs brand-name">MARISOL DUNE</div>
  <div class="abs brand-slogan">Australia's Sexiest Lingerie</div>

  <div class="abs shipping"><strong>FREE SHIPPING</strong><small>On Order over $100</small></div>
  <svg class="abs cart-icon" width="28" height="38" viewBox="0 0 28 38" aria-hidden="true">
    <path d="M9 10 V6 a5 5 0 0 1 10 0 V10" fill="none" stroke="#bbb" stroke-width="1.2"/>
    <rect x="3" y="10" width="22" height="26" fill="#fafafa" stroke="#ccc"/>
  </svg>
  <div class="abs cart">Cart :<small>0 item (s) &nbsp;- $ 0.00</small></div>

  <nav class="abs nav">
    <a class="current" href="#">HOME</a>
    <ul>
      <li>BRAS</li><li>PANTIES</li><li>SLEEP</li><li>SEXY</li><li>TOPS</li><li>SWIM</li><li>BEAUTY</li>
    </ul>
  </nav>
</header>

<section class="abs hero" role="img" aria-label="Photo of a model in a turquoise bandeau bikini on a beach under a bright blue sky">
  <div class="abs hero-figure"></div>
  <div class="abs sale-flag">
    <svg width="184" height="82" viewBox="0 0 184 82" aria-hidden="true"><polygon points="184,0 0,82 184,82" fill="var(--sale-red)"/></svg>
    <span>SALE</span>
  </div>
  <div class="abs hero-title">
    <h1>HOT SEXY SETS</h1>
    <p>STARTS FROM $125</p>
  </div>
  <a class="abs btn-dark hero-btn">SHOP NOW</a>
</section>

<section class="abs promo">
  <div class="abs promo-collections"><span class="year">2015</span> DESIGNER'S<br>LATEST COLLECTIONS</div>
  <div class="abs promo-divider"></div>
  <div class="abs promo-group promo-sale">
    <span class="promo-big">SALE</span>
    <span class="promo-sub">UPTO<br>50% OFF</span>
  </div>
  <div class="abs promo-group promo-hot">
    <span class="promo-big">HOT</span>
    <span>
      <span class="promo-sub" style="display:block">SEXY SETS</span>
      <a class="btn-dark promo-btn">SHOP NOW</a>
    </span>
  </div>
</section>

<section class="products">
  <article class="abs product" style="left:120px">
    <div class="product-photo" role="img" aria-label="Model wearing a leopard print camisole set" style="background:linear-gradient(180deg,#d9d4cf,#c9a98a 45%,#a78462 70%,#d8d2cc)"></div>
    <div class="product-name">ISpsum dolor sit amet</div>
    <div class="product-price">$96.00</div>
  </article>
  <div class="abs product-rule" style="left:284px"></div>
  <article class="abs product" style="left:310px">
    <div class="product-photo" role="img" aria-label="Model wearing a sheer brown bra and brief set" style="background:linear-gradient(180deg,#f7f7f7,#e8cdb5 35%,#7a6252 55%,#e3c7ae 80%,#f3f3f3)"></div>
    <div class="product-name">Dolor sit amet</div>
    <div class="product-price">$84.25</div>
  </article>
  <div class="abs product-rule" style="left:476px"></div>
  <article class="abs product" style="left:499px">
    <div class="product-photo" role="img" aria-label="Model wearing a pink bra and brief set" style="background:linear-gradient(180deg,#f7f7f7,#ecd0b8 35%,#cf4aa8 55%,#e6c8ad 80%,#f3f3f3)"></div>
    <div class="product-name">Dolor sit amet conse</div>
    <div class="product-price">$319.25</div>
  </article>
  <div class="abs product-rule" style="left:672px"></div>
  <article class="abs product" style="left:697px">
    <div class="product-photo" role="img" aria-label="Model wearing a sheer brown bra and brief set" style="background:linear-gradient(180deg,#f7f7f7,#e8cdb5 35%,#7a6252 55%,#e3c7ae 80%,#f3f3f3)"></div>
    <div class="product-name">Dolor sit amet</div>
    <div class="product-price">$84.25</div>
  </article>
</section>

<footer>
  <div class="abs footer"></div>
  <div class="abs footer-col" style="left:114px"><h3>INFORMATION</h3><ul><li>About</li><li>Delivery</li><li>Privacy Policy</li><li>Terms &amp; Conditions</li></ul></div>
  <div class="abs footer-col" style="left:311px"><h3>CUSTOMER SERVICE</h3><ul><li>Contact Us</li><li>Returns</li><li>Site Map</li><li>Join Us :</li></ul></div>
  <div class="abs footer-col" style="left:515px"><h3>EXTRA SERVICES</h3><ul><li>Gift Vouchers</li><li>Sales</li><li>Specials</li></ul></div>
  <div class="abs footer-col" style="left:725px"><h3>CUSTOMER ACCOUNT</h3><ul><li>My Account</li><li>Order History</li><li>Wish List</li><li>Newsletter</li></ul></div>
  <div class="abs copyright">©&nbsp; 2015 Marisol Dune.</div>
  <div class="abs social" style="left:787px; top:1171px"><span></span><span></span><span></span><span></span></div>
</footer>

</body>
</html>
```